EASY Design some Business Cards

Black and white business cards needed for photographer. see instructions attached. Please make sure files are printable! Logo is also attached

```html
<!DOCTYPE html>
<html lang="en">
<head>
<meta charset="utf-8">
<title>Lumen Frame Photography – Business Cards</title>
<link href="https://fonts.googleapis.com/css2?family=Raleway:wght@400;600;800&display=swap" rel="stylesheet">
<style>
  :root {
    --backdrop: #3a302b;
    --card: #ffffff;
    --ink: #0d0d0d;
    --ink-soft: #1a1a1a;
    --paper-text: #ffffff;
    --muted: #cfcfcf;
  }
  * { box-sizing: border-box; margin: 0; padding: 0; }
  html, body {
    width: 1200px; height: 663px; overflow: hidden;
    background: var(--backdrop);
    font-family: "Raleway", sans-serif;
  }
  .stage {
    position: relative; width: 1200px; height: 663px;
    display: flex; align-items: center; justify-content: center; gap: 60px;
  }
  .card {
    position: relative; width: 510px; height: 292px;
    background: var(--card); border-radius: 16px; overflow: hidden;
    box-shadow: 0 10px 30px rgba(0,0,0,.35);
  }

  /* Front */
  .card--front {
    display: flex; flex-direction: column; align-items: center; justify-content: center; gap: 16px;
  }
  .brand-dot { width: 120px; height: 120px; border-radius: 50%; background: var(--ink); }
  .brand-name {
    font-weight: 800; font-size: 24px; letter-spacing: 2px; color: var(--ink);
    text-transform: uppercase; text-align: center; line-height: 1.25;
  }

  /* Back */
  .band { position: absolute; inset: 0; }
  .back-brand {
    position: absolute; left: 28px; top: 70px; width: 170px;
    display: flex; flex-direction: column; align-items: center; gap: 10px;
  }
  .back-brand .brand-dot { width: 96px; height: 96px; }
  .back-brand .brand-name { font-size: 16px; letter-spacing: 1.5px; }

  .contact {
    position: absolute; left: 262px; top: 66px; color: var(--paper-text);
  }
  .contact__name { font-weight: 600; font-size: 19px; }
  .contact__role { font-size: 11px; color: var(--muted); margin-bottom: 12px; }
  .contact__list { list-style: none; }
  .contact__item {
    display: flex; align-items: center; gap: 8px;
    font-size: 11.5px; line-height: 19px;
  }
  .contact__icon { width: 11px; height: 11px; flex: none; }
  .contact__mark { width: 10px; height: 10px; background: var(--paper-text); border-radius: 2px; flex: none; }
</style>
</head>
<body>
<main class="stage">

  <section class="card card--front" aria-label="Card front">
    <div class="brand-dot"></div>
    <div class="brand-name">Lumen Frame<br>Photography</div>
  </section>

  <section class="card card--back" aria-label="Card back">
    <svg class="band" viewBox="0 0 510 292" preserveAspectRatio="none" aria-hidden="true">
      <path d="M215 40 H510 V252 H215 Q245 146 215 40 Z" fill="var(--ink)"/>
    </svg>

    <div class="back-brand">
      <div class="brand-dot"></div>
      <div class="brand-name">Lumen Frame</div>
    </div>

    <div class="contact">
      <div class="contact__name">Mister Calloway</div>
      <div class="contact__role">Photographer</div>
      <ul class="contact__list">
        <li class="contact__item">
          <svg class="contact__icon" viewBox="0 0 24 24"><path fill="#fff" d="M6.6 10.8a15.1 15.1 0 0 0 6.6 6.6l2.2-2.2c.3-.3.7-.4 1-.2 1.1.4 2.3.6 3.6.6.6 0 1 .4 1 1V20c0 .6-.4 1-1 1A17 17 0 0 1 3 4c0-.6.4-1 1-1h3.5c.6 0 1 .4 1 1 0 1.3.2 2.5.6 3.6.1.3 0 .7-.2 1z"/></svg>
          555-014-2290
        </li>
        <li class="contact__item">
          <svg class="contact__icon" viewBox="0 0 24 24"><rect x="2" y="5" width="20" height="14" rx="2" fill="none" stroke="#fff" stroke-width="2.4"/><path d="M3 6l9 7 9-7" fill="none" stroke="#fff" stroke-width="2.4"/></svg>
          lumenframephoto.com
        </li>
        <li class="contact__item">
          <svg class="contact__icon" viewBox="0 0 24 24"><circle cx="12" cy="12" r="9.5" fill="none" stroke="#fff" stroke-width="2.4"/><path d="M2.5 12h19M12 2.5c3 3 3 16 0 19M12 2.5c-3 3-3 16 0 19" fill="none" stroke="#fff" stroke-width="1.8"/></svg>
          www.lumenframephoto.com
        </li>
        <li class="contact__item"><span class="contact__mark"></span>Mister Calloway Photography</li>
        <li class="contact__item"><span class="contact__mark"></span>lumenframephoto</li>
      </ul>
    </div>
  </section>

</main>
</body>
</html>
```